Residential Construction Business - Site Signage

I need a design made for a site fence banner. We have a logo and branding so the design would need to be aligned with this. It would need to be made to specific size ratio so that it can be sent to the maker for production.
ratio : 4600 wide x 1700 high
The design should feature our website and also the slogan
"don't move, re-imagine"

Target Market(s)

potential clients

Industry/Entity Type

construction

Font styles to use
Other font styles liked:
• to match branding

Colors
0054AA
0677BA
7BADD7
CADEEF
E8F1F8

Requirements
Must have
• www.velmbuild.com.au Majority of the sign is our brand logo
Nice to have
• Majority of the sign is our brand logo
Should not have
• colors and themes that arent brand relevant

```html
<!DOCTYPE html>
<html lang="en">
<head>
<meta charset="utf-8">
<title>Velm Build – Site Fence Banner</title>
<link rel="stylesheet" href="https://fonts.googleapis.com/css2?family=Montserrat:wght@400;500;600;700&display=swap">
<style>
  :root {
    --navy: #073e5d;
    --brand-blue: #0a77ba;
    --panel: #f2f2f4;
    --panel-edge: #d6d6da;
    --page: #fefefe;
    --white: #ffffff;
  }
  * { margin: 0; padding: 0; box-sizing: border-box; }
  html, body {
    width: 1200px;
    height: 1001px;
    overflow: hidden;
    background: var(--page);
  }
  .canvas {
    position: relative;
    width: 1200px;
    height: 1001px;
    font-family: "Montserrat", Arial, sans-serif;
    line-height: 1;
  }
  .banner-shapes {
    position: absolute;
    left: 0;
    top: 0;
  }
  .canvas p, .canvas a, .canvas li { position: absolute; white-space: nowrap; }

  .slogan {
    font-size: 52px;
    font-weight: 500;
    color: var(--brand-blue);
    letter-spacing: -0.5px;
  }
  .slogan--first { left: 48px; top: 309px; }
  .slogan--second { left: 54px; top: 638px; }

  .brand-name {
    left: 123px;
    top: 478px;
    font-size: 40px;
    font-weight: 600;
    letter-spacing: 21px;
    color: var(--brand-blue);
  }

  .services {
    list-style: none;
  }
  .services li {
    left: 791px;
    font-size: 25px;
    font-weight: 600;
    letter-spacing: 8.5px;
    color: var(--navy);
  }
  .services li:nth-child(1) { top: 316px; }
  .services li:nth-child(2) { top: 345px; }
  .services li:nth-child(3) { top: 375px; }

  .contact-name, .contact-phone {
    left: 791px;
    font-size: 31px;
    font-weight: 700;
    color: var(--navy);
  }
  .contact-name { letter-spacing: 5px; }
  .contact-phone { letter-spacing: 3.5px; }
  .contact--first .contact-name { top: 450px; }
  .contact--first .contact-phone { top: 484px; }
  .contact--second .contact-name { top: 543px; }
  .contact--second .contact-phone { top: 577px; }

  .website {
    left: 791px;
    top: 665px;
    font-size: 22px;
    font-weight: 500;
    color: var(--navy);
    text-decoration: none;
  }
</style>
</head>
<body>
<main class="canvas">
  <svg class="banner-shapes" width="1200" height="1001" viewBox="0 0 1200 1001" aria-hidden="true">
    <rect class="banner-panel" x="0.5" y="272.5" width="1199" height="455" fill="var(--panel)" stroke="var(--panel-edge)" stroke-width="1"/>
    <path class="banner-chevron" d="M0 272 H480.6 L282 480 Q273 500 282 520 L488.6 728 H0 Z" fill="var(--navy)"/>
    <line class="banner-divider" x1="716" y1="318" x2="716" y2="684" stroke="var(--navy)" stroke-width="2.5"/>
  </svg>

  <p class="slogan slogan--first">“Don’t Move,</p>
  <p class="slogan slogan--second">Re-Imagine”</p>

  <p class="brand-name">VELM BUILD</p>

  <ul class="services">
    <li>NEW HOMES</li>
    <li>RENOVATIONS</li>
    <li>ADDITIONS</li>
  </ul>

  <div class="contact contact--first">
    <p class="contact-name">DANIEL HARTLEY</p>
    <p class="contact-phone">0412 867 309</p>
  </div>
  <div class="contact contact--second">
    <p class="contact-name">OWEN MARSH</p>
    <p class="contact-phone">0455 128 740</p>
  </div>

  <a class="website" href="#">www.velmbuild.com.au</a>
</main>
</body>
</html>
```